Premium label design for product needed

UPDATE: (Scroll down)
For a face care product i need a new front label on the bottle. The current one is white and i want to add the franchise color green. The objective is to premiunize the packaging and to give guidance to the consumers to find their franchise color. The task is to find several option to color the label on the bottle in the most premium way. But at the same time it should not be playful, more in a serious medical direction or in a counterbrand direction. It should look absolutely premium. but should not shout to much. The text structure should remain the same. I will provide a powerpoint slide to illustrate the task even clearer.
UPDATE: DO NOT DESIGN THE FOLDING BOX, only design the bottle. The folding box only serves the purpose of giving the text/layout structure and rough color intent.

Target Market(s)

female 25-39

Requirements
Must have
• Premium, Uniqueness, Innovative

```html
<!DOCTYPE html>
<html lang="en">
<head>
<meta charset="utf-8">
<title>Pure Skin Solution – Face Care Label</title>
<link rel="stylesheet" href="https://fonts.googleapis.com/css2?family=Open+Sans:wght@400;600&family=Noto+Serif:wght@400&display=swap">
<style>
  :root {
    --bg-top: #ffffff;
    --bg-bottom: #d6d6d6;
    --panel: #f7f7f7;
    --panel-shade: #e6e6e6;
    --green: #66e177;
    --green-band-start: #b5dcb3;
    --green-band-end: #7ec97d;
    --ink: #1c2b2b;
    --ink-soft: #2f3a3a;
  }
  * { margin: 0; padding: 0; box-sizing: border-box; }
  html, body { width: 1200px; height: 1200px; overflow: hidden; }
  body {
    position: relative;
    background: linear-gradient(180deg, var(--bg-top) 0%, var(--bg-top) 12%, var(--bg-bottom) 100%);
    font-family: "Open Sans", sans-serif;
    color: var(--ink);
  }

  /* ---------- Carton front panel ---------- */
  .carton {
    position: absolute;
    left: 330px; top: 194px;
    width: 282px; height: 854px;
    background: linear-gradient(90deg, var(--panel-shade) 0%, var(--panel) 30%, #ffffff 55%, var(--panel-shade) 100%);
  }
  .carton__cap {
    position: absolute; left: 0; top: 0;
    width: 100%; height: 46px;
    background: var(--green);
  }
  .carton__brand {
    position: absolute;
    left: 160px; top: 84px;
    width: 260px; height: 90px;
    transform-origin: 0 0;
    transform: rotate(-90deg) translate(-260px, 0);
  }
  .carton__brand .brand-name {
    display: block;
    font-size: 52px; font-weight: 400; letter-spacing: 0;
    line-height: 1; color: var(--ink);
    white-space: nowrap;
  }
  .carton__brand .brand-sub {
    display: flex; align-items: center; gap: 8px;
    margin-top: 6px;
    font-size: 22px; letter-spacing: 5px;
  }
  .brand-mark {
    display: inline-block;
    width: 12px; height: 12px;
    background: var(--green);
  }
  .carton__claims {
    position: absolute; left: 22px; top: 434px;
    font-size: 18px; letter-spacing: 2px; line-height: 25px;
    color: var(--ink-soft);
  }
  .carton__band {
    position: absolute; left: 0; top: 505px;
    width: 100%; height: 94px;
    background: linear-gradient(90deg, var(--green-band-start), var(--green-band-end));
    padding: 14px 0 0 22px;
  }
  .band__small { font-size: 25px; letter-spacing: 1.5px; line-height: 28px; }
  .band__large { font-size: 33px; letter-spacing: 3px; line-height: 36px; }
  .carton__copy {
    position: absolute; left: 22px; top: 648px;
    width: 220px;
    font-size: 10px; line-height: 18px; color: #222;
  }
  .carton__footer {
    position: absolute; left: 23px; top: 742px;
    font-family: "Noto Serif", serif;
    font-size: 19px; letter-spacing: 2.5px; line-height: 25px;
    color: var(--ink-soft);
  }
  .carton__volume { margin-top: 10px; }

  /* ---------- Bottle front label ---------- */
  .bottle {
    position: absolute;
    left: 665px; top: 318px;
    width: 223px; height: 714px;
    border-radius: 10px 10px 4px 4px;
    background: linear-gradient(90deg, #ececec 0%, #ffffff 25%, #fbfbfb 70%, #e4e4e4 100%);
  }
  .bottle__cap-line {
    position: absolute; left: 0; top: 200px;
    width: 100%; height: 1px; background: #e2e2e2;
  }
  .bottle__brand {
    position: absolute; left: 21px; top: 308px;
  }
  .bottle__brand .brand-name {
    font-size: 33px; line-height: 1; color: var(--ink); white-space: nowrap;
  }
  .bottle__brand .brand-sub {
    display: flex; align-items: center; gap: 6px;
    margin-top: 4px;
    font-size: 15px; letter-spacing: 3px;
  }
  .bottle__brand .brand-mark { width: 9px; height: 9px; }
  .bottle__claims {
    position: absolute; left: 16px; top: 430px;
    font-size: 13px; font-weight: 600; letter-spacing: 1.3px; line-height: 18px;
    color: var(--ink-soft);
  }
  .bottle__band {
    position: absolute; left: 0; top: 480px;
    width: 100%; height: 73px;
    background: linear-gradient(90deg, var(--green-band-start), var(--green-band-end));
    padding: 12px 0 0 16px;
  }
  .bottle__band .band__small { font-size: 20px; line-height: 23px; letter-spacing: 1.5px; }
  .bottle__band .band__large { font-size: 26px; line-height: 30px; letter-spacing: 3px; }
  .bottle__variant {
    position: absolute; left: 16px; top: 567px;
    font-size: 12px; letter-spacing: 3px; color: var(--ink-soft);
  }
  .bottle__footer {
    position: absolute; left: 16px; top: 610px;
    font-family: "Noto Serif", serif;
    font-size: 14px; letter-spacing: 2px; line-height: 19px;
    color: var(--ink-soft);
  }
  .bottle__volume { margin-top: 26px; font-size: 15px; }
</style>
</head>
<body>

  <section class="carton" aria-label="Carton front panel">
    <div class="carton__cap"></div>
    <div class="carton__brand">
      <span class="brand-name">PURE SKIN</span>
      <span class="brand-sub">SOLUTION <span class="brand-mark"></span></span>
    </div>
    <p class="carton__claims">ACNE<br>OIL CONTROL</p>
    <div class="carton__band">
      <p class="band__small">COMPLETE</p>
      <p class="band__large">FACE CARE</p>
    </div>
    <p class="carton__copy">Lorem Ipsum is simply dummy textLorem Ipsum is simply dummy text Lorem Ipsum is simply dummy text</p>
    <div class="carton__footer">
      <p>DERMATOLOGYCAL<br>SKINCARE</p>
      <p class="carton__volume">20 ML</p>
    </div>
  </section>

  <section class="bottle" aria-label="Bottle front label">
    <div class="bottle__cap-line"></div>
    <div class="bottle__brand">
      <p class="brand-name">PURE SKIN</p>
      <p class="brand-sub">SOLUTION <span class="brand-mark"></span></p>
    </div>
    <p class="bottle__claims">ACNE<br>OIL CONTROL</p>
    <div class="bottle__band">
      <p class="band__small">COMPLETE</p>
      <p class="band__large">FACE CARE</p>
    </div>
    <p class="bottle__variant">A.I. MATT FLUID</p>
    <div class="bottle__footer">
      <p>DERMATOLOGYCAL<br>SKINCARE</p>
      <p class="bottle__volume">20 ML</p>
    </div>
  </section>

</body>
</html>
```